Poster/flyer design needed for Choral Concert

Please include the following text:<br/>Title of Event: Raise the Rafters!<br/>Subtitle: A Choral Festival of Song to celebrate Kinship Fortnight<br/>Wattlecombe choirs come together to share their unique and beautiful music.<br/>Date: Sat March 21st 2020<br/>Time: 2pm - 4pm<br/>Venue: Tullaby Mechanics Hall<br/>Tickets: $10 each. Proceeds to Bushland Relief & TBF Crews<br/>Hosted By Lifted Tunes<br/>Featuring:<br/>Merrigal Unaccompanied Ladies' Chorus<br/>Wine of Dusk<br/>Kerrabee Neighbourhood Chorus<br/>Chant Together<br/>* design required for A4 poster and DL flyer (may be modified)<br/>* Please use orange as the main colour<br/>* The Kinship fortnight logo must be included (see attached - either is fine). The frame may be useful as well.<br/>* Please include musical images<br/>* Visit kinshipday.example.au for info on Kinship Fortnight

Target Market(s)

music-lovers, community-minded people, residents of the area, probably 30 + age

Industry/Entity Type

Entertainment

Font styles to use
Serif
Sans Serif

Colors
f78f20
ffffff

Requirements
Must have
• Orange colour
• Kinship logo
• required text
Nice to have
• A musical theme
Should not have
• writing should not be too small and difficult to read

```html
<!DOCTYPE html>
<html lang="en">
<head>
<meta charset="utf-8">
<title>Raise the Rafters! – Poster and DL Flyer</title>
<link rel="stylesheet" href="https://fonts.googleapis.com/css2?family=Arimo:wght@400;700&family=Oswald:wght@500;600&display=swap">
<style>
  :root {
    --orange: #f7941d;
    --orange-deep: #e9821a;
    --white: #ffffff;
    --ink: #111111;
    --stage: #e6e6e4;
    --photo-dark: #2a2220;
    --photo-warm: #6b4a3a;
    --text-font: "Arimo", Arial, sans-serif;
    --badge-font: "Oswald", "Arial Narrow", sans-serif;
  }
  * { box-sizing: border-box; margin: 0; padding: 0; }
  html, body { width: 1200px; height: 1049px; overflow: hidden; }
  body { background: var(--stage); font-family: var(--text-font); position: relative; }

  .sheet { position: absolute; background: var(--white); overflow: hidden; box-shadow: 0 4px 14px rgba(0,0,0,.25); }
  .sheet > * { position: absolute; }
  .poster { left: 95px; top: 88px; width: 595px; height: 842px; }
  .flyer { left: 803px; top: 205px; width: 253px; height: 593px; }

  .hero-photo { background: radial-gradient(ellipse at 55% 55%, var(--photo-warm) 0%, #4a3328 40%, var(--photo-dark) 85%); }
  .frame { left: 0; top: 0; width: 100%; height: 100%; }

  .event-brand { font-weight: 700; color: var(--ink); line-height: .92; text-transform: uppercase; letter-spacing: -.5px; text-align: right; white-space: nowrap; }
  .event-date { color: var(--orange); font-weight: 700; text-align: center; line-height: .85; }
  .event-date .day { display: block; }
  .event-date .month { display: block; }

  .title { color: var(--white); font-weight: 700; text-align: center; text-transform: uppercase; line-height: 1.15; text-shadow: 0 2px 6px rgba(0,0,0,.5); }

  .ticket-badge { border-radius: 50%; background: var(--ink); border: 3px solid var(--white); color: var(--white); text-align: center; display: flex; flex-direction: column; justify-content: center; align-items: center; box-shadow: 0 3px 8px rgba(0,0,0,.4); }
  .ticket-badge .label { font-weight: 700; }
  .ticket-badge .price { font-family: var(--badge-font); font-weight: 600; line-height: 1; white-space: nowrap; }
  .ticket-badge .note { line-height: 1.15; }

  .subtitle { color: var(--white); font-weight: 700; text-align: center; text-transform: uppercase; line-height: 1.18; width: 100%; left: 0; }
  .tagline-ribbon { background: var(--ink); color: var(--white); text-align: center; display: flex; align-items: center; justify-content: center; box-shadow: 0 2px 4px rgba(0,0,0,.35); white-space: nowrap; }
  .details { color: var(--ink); font-weight: 700; text-align: center; width: 100%; left: 0; }
  .host-box { border: 1.5px solid var(--white); color: var(--white); font-weight: 700; display: flex; align-items: center; justify-content: center; }

  .choir { text-align: center; }
  .choir-photo { border-radius: 50%; border: 3px solid var(--white); box-shadow: 0 2px 5px rgba(0,0,0,.35); margin: 0 auto; }
  .choir-photo.group { background: radial-gradient(circle at 50% 60%, #4e5a66, #2c2a2e); }
  .choir-photo.food { background: radial-gradient(circle at 50% 50%, #b9a27a, #6f5d4a); }
  .choir-photo.yellow { background: radial-gradient(circle at 50% 55%, #c9b240, #2f2b30 70%); }
  .choir-photo.blue { background: radial-gradient(circle at 50% 55%, #5f88a8, #363b44 75%); }
  .choir-name { color: var(--ink); line-height: 1.15; }

  .footer { left: 0; width: 100%; background: var(--white); display: flex; align-items: center; justify-content: center; }
  .figure-row { background: linear-gradient(90deg, #f6a04d, #9ad0e0, #c8a4d8, #8fcf9a, #f28b8b, #7fb2e5); opacity: .75; border-radius: 3px; }
  .footer-brand { text-align: center; }
  .footer-brand .name { color: var(--orange); font-weight: 700; text-transform: uppercase; display: block; }
  .footer-brand .site { color: var(--ink); font-weight: 700; display: block; }

  /* Poster sizes */
  .poster .event-brand { right: 268px; top: 22px; font-size: 34px; }
  .poster .event-date { left: 340px; top: 10px; width: 96px; }
  .poster .event-date .day { font-size: 72px; }
  .poster .event-date .month { font-size: 24px; }
  .poster .hero-photo { left: 0; top: 95px; width: 595px; height: 345px; }
  .poster .title { left: 30px; top: 192px; width: 510px; font-size: 50px; }
  .poster .ticket-badge { left: 440px; top: 302px; width: 130px; height: 130px; }
  .poster .ticket-badge .label { font-size: 11px; }
  .poster .ticket-badge .price { font-size: 26px; margin: 3px 0; }
  .poster .ticket-badge .note { font-size: 10px; width: 100px; }
  .poster .subtitle { top: 465px; font-size: 24px; }
  .poster .tagline-ribbon { left: 23px; top: 534px; width: 550px; height: 34px; font-size: 15px; }
  .poster .details { top: 581px; font-size: 16px; }
  .poster .host-box { left: 167px; top: 614px; width: 254px; height: 26px; font-size: 15px; }
  .poster .choir { top: 660px; width: 120px; }
  .poster .choir-photo { width: 88px; height: 88px; }
  .poster .choir-name { font-size: 10px; margin-top: 6px; }
  .poster .footer { top: 787px; height: 55px; gap: 18px; }
  .poster .figure-row { width: 175px; height: 28px; }
  .poster .footer-brand .name { font-size: 17px; }
  .poster .footer-brand .site { font-size: 15px; }

  /* Flyer sizes */
  .flyer .event-brand { right: 105px; top: 22px; font-size: 17px; }
  .flyer .event-date { left: 158px; top: 16px; width: 56px; }
  .flyer .event-date .day { font-size: 38px; }
  .flyer .event-date .month { font-size: 13px; }
  .flyer .hero-photo { left: 0; top: 92px; width: 253px; height: 230px; }
  .flyer .title { left: 10px; top: 158px; width: 233px; font-size: 25px; }
  .flyer .ticket-badge { left: 160px; top: 238px; width: 86px; height: 86px; border-width: 2px; }
  .flyer .ticket-badge .label { font-size: 7px; }
  .flyer .ticket-badge .price { font-size: 17px; margin: 2px 0; }
  .flyer .ticket-badge .note { font-size: 6.5px; width: 62px; }
  .flyer .subtitle { top: 344px; font-size: 13px; }
  .flyer .tagline-ribbon { left: 10px; top: 392px; width: 233px; height: 14px; font-size: 6.5px; }
  .flyer .details { font-size: 9px; }
  .flyer .details.when { top: 414px; }
  .flyer .details.where { top: 433px; }
  .flyer .rule { left: 50px; top: 428px; width: 153px; height: 1px; background: var(--white); }
  .flyer .host-box { left: 55px; top: 452px; width: 143px; height: 16px; font-size: 9px; border-width: 1px; }
  .flyer .choir { top: 478px; width: 60px; }
  .flyer .choir-photo { width: 52px; height: 52px; border-width: 2px; }
  .flyer .choir-name { font-size: 6px; margin-top: 3px; }
  .flyer .footer { top: 555px; height: 38px; gap: 6px; }
  .flyer .figure-row { width: 70px; height: 16px; }
  .flyer .footer-brand .name { font-size: 9px; }
  .flyer .footer-brand .site { font-size: 8px; }
</style>
</head>
<body>

<article class="sheet poster">
  <div class="hero-photo" role="img" aria-label="Photo of many hands of different skin tones meeting in the centre, wearing bracelets"></div>
  <svg class="frame" viewBox="0 0 595 842" aria-hidden="true">
    <path d="M0 0 H595 V100 Q300 84 0 118 Z" fill="var(--white)"/>
    <path d="M0 118 Q300 84 595 100 V110 Q300 96 0 130 Z" fill="var(--ink)"/>
    <path d="M0 418 Q270 385 595 398 V842 H0 Z" fill="var(--white)"/>
    <path d="M0 422 Q270 392 595 405 V410 Q270 402 0 430 Z" fill="var(--ink)"/>
    <path d="M0 438 Q270 412 595 420 V787 H0 Z" fill="var(--orange)"/>
  </svg>

  <div class="event-brand">Kinship<br>Fortnight</div>
  <div class="event-date"><span class="day">21</span><span class="month">MARCH</span></div>

  <h1 class="title">Raise the<br>Rafters!</h1>

  <div class="ticket-badge">
    <span class="label">TICKETS:</span>
    <span class="price">$10 EACH</span>
    <span class="note">Proceeds to Bushland Relief &amp; TBF Crews</span>
  </div>

  <h2 class="subtitle">A Choral Festival of Song<br>to Celebrate Kinship Fortnight</h2>
  <p class="tagline-ribbon">Wattlecombe choirs come together to share their unique and beautiful music.</p>
  <p class="details">Sat March 21st 2020 | 2pm - 4pm | Tullaby Mechanics Hall</p>
  <p class="host-box">Hosted By Lifted Tunes</p>

  <div class="choir" style="left:42px"><div class="choir-photo group" role="img" aria-label="Photo of the ladies' chorus"></div><p class="choir-name">Merrigal Unaccompanied<br>Ladies' Chorus</p></div>
  <div class="choir" style="left:161px"><div class="choir-photo food" role="img" aria-label="Photo of a shared food platter"></div><p class="choir-name">Wine of Dusk</p></div>
  <div class="choir" style="left:297px"><div class="choir-photo yellow" role="img" aria-label="Photo of the neighbourhood chorus in yellow scarves"></div><p class="choir-name">Kerrabee Neighbourhood<br>Chorus</p></div>
  <div class="choir" style="left:413px"><div class="choir-photo blue" role="img" aria-label="Photo of singers in blue shirts"></div><p class="choir-name">Chant Together</p></div>

  <footer class="footer">
    <div class="figure-row" role="img" aria-label="Row of colourful paper-chain people holding hands"></div>
    <div class="footer-brand"><span class="name">Kinship Fortnight</span><span class="site">kinshipday.example.au</span></div>
    <div class="figure-row" role="img" aria-label="Row of colourful paper-chain people holding hands"></div>
  </footer>
</article>

<article class="sheet flyer">
  <div class="hero-photo" role="img" aria-label="Photo of many hands of different skin tones meeting in the centre, wearing bracelets"></div>
  <svg class="frame" viewBox="0 0 253 593" aria-hidden="true">
    <path d="M0 0 H253 V88 Q130 80 0 100 Z" fill="var(--white)"/>
    <path d="M0 100 Q130 80 253 88 V94 Q130 88 0 106 Z" fill="var(--ink)"/>
    <path d="M0 304 Q120 285 253 292 V593 H0 Z" fill="var(--white)"/>
    <path d="M0 307 Q120 290 253 296 V299 Q120 295 0 312 Z" fill="var(--ink)"/>
    <path d="M0 318 Q120 302 253 306 V555 H0 Z" fill="var(--orange)"/>
  </svg>

  <div class="event-brand">Kinship<br>Fortnight</div>
  <div class="event-date"><span class="day">21</span><span class="month">MARCH</span></div>

  <h1 class="title">Raise the<br>Rafters!</h1>

  <div class="ticket-badge">
    <span class="label">TICKETS:</span>
    <span class="price">$10 EACH</span>
    <span class="note">Proceeds to Bushland Relief &amp; TBF Crews</span>
  </div>

  <h2 class="subtitle">A Choral Festival of Song<br>to Celebrate Kinship Fortnight</h2>
  <p class="tagline-ribbon">Wattlecombe choirs come together to share their unique and beautiful music.</p>
  <p class="details when">Sat March 21st 2020 from 2pm - 4pm</p>
  <div class="rule"></div>
  <p class="details where">Tullaby Mechanics Hall</p>
  <p class="host-box">Hosted By Lifted Tunes</p>

  <div class="choir" style="left:10px"><div class="choir-photo group" role="img" aria-label="Photo of the ladies' chorus"></div><p class="choir-name">Merrigal Unaccompanied<br>Ladies' Chorus</p></div>
  <div class="choir" style="left:71px"><div class="choir-photo food" role="img" aria-label="Photo of a shared food platter"></div><p class="choir-name">Wine of Dusk</p></div>
  <div class="choir" style="left:134px"><div class="choir-photo yellow" role="img" aria-label="Photo of the neighbourhood chorus in yellow scarves"></div><p class="choir-name">Kerrabee Neighbourhood<br>Chorus</p></div>
  <div class="choir" style="left:190px"><div class="choir-photo blue" role="img" aria-label="Photo of singers in blue shirts"></div><p class="choir-name">Chant Together</p></div>

  <footer class="footer">
    <div class="figure-row" role="img" aria-label="Row of colourful paper-chain people holding hands"></div>
    <div class="footer-brand"><span class="name">Kinship Fortnight</span><span class="site">kinshipday.example.au</span></div>
    <div class="figure-row" role="img" aria-label="Row of colourful paper-chain people holding hands"></div>
  </footer>
</article>

</body>
</html>
```